New Business Card Design Project

hello again,
i have an awful year and we were not able to complete our logo plan. we would like to use our #1 logo for business card design process. the primary colors for business card should be white background with orange & black letters. our business is mobil truck cranes. we deliver heavy stuff and unload cargo with crane that is mounted on our trucks.
here is our business card info:
HARBORLINE LIFT HAULERS, INC.
482 WICKHAM AVE
ASHCOMBE, VT 05999
OFFICE - 516 430 2291
DIRECT - 1 888 LIFT HAULS
GERALD@HLHAUL.EXAMPLE
PLEASE also try to get our slogan on card .... "Our Loads Keep Climbin"
lastly please also put "24 hour Knuckleboom Service"
you can call me anytime 24/7 to discuss...my cell # is: 516 907 4463
please also list: Gerald Pruitt, President
Target Market(s)
Heavy Construction industry
Industry/Entity Type
heavy construction industry
Contact Information for Business Card
24 Hr Knuckleboom Service

```html
<!DOCTYPE html>
<html lang="en">
<head>
<meta charset="utf-8">
<title>Harborline Lift Haulers – Business Card</title>
<link href="https://fonts.googleapis.com/css2?family=Varela+Round&display=swap" rel="stylesheet">
<style>
  :root {
    --bg: #8a8a8a;
    --card: #ffffff;
    --ink: #1c1c1c;
    --orange: #f7861e;
    --sky-light: #ececec;
    --sky-mid: #cfcfcf;
    --divider: #e4e4e4;
  }
  * { margin: 0; padding: 0; box-sizing: border-box; }
  html, body { width: 1200px; height: 876px; overflow: hidden; }
  body {
    background: var(--bg);
    font-family: "Varela Round", sans-serif;
    color: var(--ink);
    position: relative;
  }
  .card {
    position: absolute;
    left: 320px;
    width: 560px;
    height: 320px;
    background: var(--card);
    overflow: hidden;
    box-shadow: 0 6px 18px rgba(0,0,0,.28);
  }
  .card--front { top: 70px; }
  .card--back { top: 470px; }

  .skyline {
    position: absolute;
    left: 0;
    bottom: 0;
    background: linear-gradient(to top, var(--sky-mid), var(--sky-light) 70%, rgba(255,255,255,0));
  }
  .card--front .skyline { width: 170px; height: 210px; }
  .card--back .skyline { width: 249px; height: 150px; }

  .brand {
    display: flex;
    align-items: center;
    gap: 10px;
    color: var(--ink);
    line-height: 1.15;
  }
  .brand__mark { background: var(--orange); flex: none; }

  .front-lockup {
    position: absolute;
    left: 200px;
    right: 30px;
    top: 92px;
  }
  .front-lockup .brand { font-size: 26px; }
  .front-lockup .brand__mark { width: 18px; height: 18px; }
  .email {
    margin-top: 22px;
    padding-left: 28px;
    font-size: 13px;
    letter-spacing: 4px;
  }

  .panel-left {
    position: absolute;
    left: 0; top: 0;
    width: 250px; height: 100%;
    border-right: 1px solid var(--divider);
  }
  .panel-left .brand {
    position: absolute;
    top: 34px;
    left: 18px; right: 14px;
    font-size: 18px;
  }
  .panel-left .brand__mark { width: 12px; height: 12px; }
  .slogan {
    position: absolute;
    top: 92px; left: 40px;
    background: var(--orange);
    color: #fff;
    font-size: 12px;
    padding: 5px 12px;
    text-transform: uppercase;
  }
  .service {
    position: absolute;
    top: 122px; left: 40px;
    font-size: 11px;
  }

  .panel-right {
    position: absolute;
    left: 282px; top: 40px;
    right: 20px;
  }
  .company { font-weight: normal; line-height: 1.25; }
  .company__line1 { display: block; font-size: 20px; color: var(--ink); }
  .company__line2 { display: block; font-size: 22px; color: var(--orange); }
  .contacts { list-style: none; margin-top: 22px; font-size: 11px; line-height: 1.7; }
  .contacts li { display: flex; align-items: center; gap: 6px; }
  .contacts svg { width: 10px; height: 10px; flex: none; }
  .contacts .plain { padding-left: 16px; }
  .note { margin-top: 14px; font-size: 12px; line-height: 1.5; }
</style>
</head>
<body>

<section class="card card--front">
  <div class="skyline" role="img" aria-label="Faint grey city skyline illustration with skyscrapers and harbour statue"></div>
  <div class="front-lockup">
    <div class="brand"><span class="brand__mark"></span>HARBORLINE LIFT HAULERS, INC.</div>
    <p class="email">gerald@hlhaul.example</p>
  </div>
</section>

<section class="card card--back">
  <div class="panel-left">
    <div class="skyline" role="img" aria-label="Faint grey city skyline illustration with skyscrapers and harbour statue"></div>
    <div class="brand"><span class="brand__mark"></span>HARBORLINE LIFT HAULERS, INC.</div>
    <p class="slogan">Our Loads Keep Climbin</p>
    <p class="service">24 hour Knuckleboom Service</p>
  </div>
  <div class="panel-right">
    <h1 class="company">
      <span class="company__line1">HARBORLINE</span>
      <span class="company__line2">LIFT HAULERS, INC.</span>
    </h1>
    <ul class="contacts">
      <li>
        <svg viewBox="0 0 10 10" aria-hidden="true"><path d="M2 0.5 L3.6 2.6 L2.6 3.8 Q3.6 6 6.2 7.4 L7.4 6.4 L9.5 8 L8.4 9.5 Q3 9 0.5 1.6 Z" fill="var(--orange)"/></svg>
        516 430 2291
      </li>
      <li>
        <svg viewBox="0 0 10 10" aria-hidden="true"><path d="M5 0.5 A3.2 3.2 0 0 1 8.2 3.7 C8.2 6 5 9.5 5 9.5 C5 9.5 1.8 6 1.8 3.7 A3.2 3.2 0 0 1 5 0.5 Z" fill="var(--orange)"/><circle cx="5" cy="3.7" r="1.2" fill="#fff"/></svg>
        482 wickham ave , ashcombe, vt 05999
      </li>
      <li class="plain">direct - 1 888 lift hauls</li>
    </ul>
    <p class="note">you can call me anytime 24/7 to discuss<br>my cell # is: 516 907 4463</p>
  </div>
</section>

</body>
</html>
```